Email Flyer for Business Re-Brand

We have re-branded from Marlowe Conveyancing to HLQ and we want to let all of our clients know, with a professional email flyer.

I want it to have the same layout as the attached flyer made by Quillbrook Printing, but the fonts and obviously the images will be different.

I have attached a document for the text.
I have also attached our logo files. (old and new)

The colour of our logo is orange, but I don't want the flyer to be heavily orange. White and grey with orange accents would be best.

Thank you.

Industry/Entity Type

Business

Font styles to use
Sans Serif

Colors
f78f20
ffffff
d9d9d9

Requirements
Must have
• Must look clean, modern and professional.
Nice to have
• Would be great to have the custom headings like in the sample, and social media icons.
Should not have
• Should not look gaudy or tacky.

```html
<!DOCTYPE html>
<html lang="en">
<head>
<meta charset="utf-8">
<title>Marlowe Conveyancing has become HLQ</title>
<link rel="stylesheet" href="https://fonts.googleapis.com/css2?family=Baloo+2:wght@500;600;700&family=PT+Sans:wght@400;700&family=Montserrat:wght@700&display=swap">
<style>
  :root{
    --orange:#f78f20;
    --white:#ffffff;
    --light-grey:#d9d9d9;
    --panel-grey:#f2f2f2;
    --heading-grey:#a9a9a9;
    --ink:#1f1f1f;
    --link:#1a9ad6;
    --banner-dark:#1c1c1c;
  }
  *{box-sizing:border-box;margin:0;padding:0}
  html,body{width:846px;height:1200px;overflow:hidden;background:var(--white)}
  .flyer{position:relative;width:846px;height:1200px;background:var(--white);font-family:"PT Sans",sans-serif;color:var(--ink)}

  .old-mark{position:absolute;top:14px;left:0;width:846px;display:flex;flex-direction:column;align-items:center;gap:6px}
  .old-mark__dot{width:66px;height:66px;border-radius:50%;background:var(--orange)}
  .old-mark__name{font-family:"PT Sans",sans-serif;font-size:10px;color:var(--heading-grey);letter-spacing:1.5px;text-transform:uppercase}

  .old-name{position:absolute;top:120px;left:0;width:846px;text-align:center;font-family:"Baloo 2",sans-serif;font-weight:700;font-size:36px;letter-spacing:1px;color:var(--heading-grey)}

  .banner{position:absolute;top:173px;left:0;width:846px;height:278px;background:linear-gradient(180deg,#2a2a2a 0%,var(--banner-dark) 50%,#262626 100%)}
  .banner__tagline{position:absolute;top:16px;left:0;width:846px;text-align:center;font-family:"Baloo 2",sans-serif;font-weight:700;font-size:31px;color:var(--white)}
  .banner__tagline strong{color:var(--orange)}
  .banner__brand{position:absolute;top:94px;left:48px;display:flex;align-items:center;gap:34px}
  .banner__square{width:150px;height:150px;border:6px solid var(--orange)}
  .banner__wordmark{color:#bdbdbd;font-family:"Montserrat",sans-serif;font-weight:700}
  .banner__wordmark-main{display:block;font-size:76px;letter-spacing:38px;line-height:1}
  .banner__wordmark-sub{display:block;font-size:22px;letter-spacing:13px;margin-top:18px}

  .divider{position:absolute;left:421px;width:5px;background:var(--light-grey)}
  .divider--top{top:500px;height:258px}
  .divider--bottom{top:872px;height:259px}

  .section-title{position:absolute;font-family:"Baloo 2",sans-serif;font-weight:600;font-size:36px;color:var(--heading-grey);text-align:center;line-height:1}
  .body-copy{position:absolute;font-size:19px;line-height:27px;text-align:justify}

  .brand-mark{position:absolute;top:526px;left:156px;width:104px;height:92px;display:flex;align-items:center;justify-content:center;gap:8px}
  .brand-mark__square{width:16px;height:16px;background:var(--orange)}
  .brand-mark__name{font-family:"PT Sans",sans-serif;font-weight:700;font-size:38px;color:var(--orange)}

  .web-address{position:absolute;top:537px;left:440px;width:406px;text-align:center;font-family:"Baloo 2",sans-serif;font-weight:600;font-size:52px;line-height:1;color:var(--orange)}
  .web-link{position:absolute;top:740px;left:440px;width:390px;text-align:center;font-weight:700;font-size:19px;color:var(--link);text-decoration:none}

  .portal-art{position:absolute;top:843px;left:150px;width:114px;height:70px;background:linear-gradient(90deg,var(--orange) 0%,#f5b06a 50%,var(--light-grey) 100%);opacity:.85}

  .social-panel{position:absolute;top:870px;left:441px;width:368px;height:110px;background:var(--panel-grey);display:flex;align-items:center;justify-content:center;gap:8px}
  .social-panel__circle{width:74px;height:74px;border-radius:50%;background:var(--white);border:2px solid var(--light-grey);display:flex;align-items:center;justify-content:center;font-family:"PT Sans",sans-serif;font-weight:700;font-size:12px;color:var(--heading-grey)}

  .footer{position:absolute;top:1153px;left:0;width:846px;height:47px;background:var(--orange);color:var(--white);text-align:center;font-family:"Baloo 2",sans-serif;font-weight:600;font-size:30px;line-height:50px}
</style>
</head>
<body>
<main class="flyer">

  <div class="old-mark">
    <span class="old-mark__dot"></span>
    <span class="old-mark__name">Marlowe Conveyancing</span>
  </div>
  <h1 class="old-name">MARLOWE CONVEYANCING</h1>

  <section class="banner" role="img" aria-label="Dark stone wall texture behind the new brand name">
    <p class="banner__tagline">has proudly become <strong>HLQ</strong></p>
    <div class="banner__brand">
      <span class="banner__square"></span>
      <p class="banner__wordmark">
        <span class="banner__wordmark-main">HLQ</span>
        <span class="banner__wordmark-sub">PROPERTY TRANSFERS</span>
      </p>
    </div>
  </section>

  <h2 class="section-title" style="top:480px;left:30px;width:360px">A New Brand</h2>
  <div class="brand-mark">
    <span class="brand-mark__square"></span>
    <span class="brand-mark__name">HLQ</span>
  </div>
  <p class="body-copy" style="top:626px;left:26px;width:364px">This past year was an incredible one for Marlowe Conveyancing. It's time to really focus our efforts &amp; the first step was a major rebrand. We're the same great people with the same great service.</p>

  <span class="divider divider--top"></span>

  <h2 class="section-title" style="top:480px;left:456px;width:360px">A New Website</h2>
  <p class="web-address">www.hlqpt.com</p>
  <p class="body-copy" style="top:626px;left:458px;width:362px;text-align:left">With a brand new name comes a brand new website, solely focused on what we do best... property transfers.</p>
  <a class="web-link" href="#">Visit the new website.</a>

  <h2 class="section-title" style="top:802px;left:30px;width:360px">A Property Portal</h2>
  <div class="portal-art" role="img" aria-label="Illustration of a house beside a flight of stairs"></div>
  <p class="body-copy" style="top:919px;left:26px;width:356px;font-size:18px">Stay tuned for our state of the art Property Portal. We couldn't think of a better way to commemorate these changes than to build a portal that will make buying and selling properties even easier for our clients. You can check progress on all your matters with our matter tracker, receive SMS updates and reminders, and much more.</p>

  <span class="divider divider--bottom"></span>

  <h2 class="section-title" style="top:802px;left:456px;width:360px">Tell Your Friends</h2>
  <div class="social-panel" aria-label="Social media links">
    <span class="social-panel__circle">Chirpline</span>
    <span class="social-panel__circle">Facet</span>
    <span class="social-panel__circle">Snaply</span>
    <span class="social-panel__circle">Reelo</span>
  </div>
  <p class="body-copy" style="top:996px;left:458px;width:358px">We're excited about the changes and we hope you are too. If you want the world to know about our new name, our new portal and our great prices, please spread the word to your friends!</p>

  <footer class="footer">www.hlqpt.com</footer>
</main>
</body>
</html>
```